ONE PAGE WEB DESIGN NEEDED for Finance Company

We need a web design (ONE PAGE DESIGN ONLY) for a new finance website called Brightwell Lending. Brightwell Lending helps customers get the right loan, whether its a home loan, investment loan, business loan etc.

You are required to come up with just the homepage design. Professionalism and quality is the key factors in the successful design.

Here are a few design questions to help you out:

-
What information should be used on the page?
Ive provided a document which outlines all the information needed to put on homepage (attached to the brief - called brightwell_page_info). Also see the Must Have section below on this brief.

-
What links should appear in the navigation/footer?:
The navigation should provide links to the following pages (NOTE: services link has subcategories):
1 Homepage
2 Services
- Home loans
- Investment loans
- Refinancing loans
- Business loans
3 About Us
4 FAQ
5 Contact Us

-
What colors should be used in the design?
Our company colors - Cyan: #2EADE3, Blue: #004B70, White. Feel free to submit designs with slight variations if you feel it improves the design.

-
What should the layout of the page be?
This is up to you to come up with - we are open to different layouts for the page design (as long as they capture the information effectively and making it easy to understand).

Target Market(s)

Potential Home owners, Families and Business Owners

Industry/Entity Type

Business

Requirements
Must have
• - Must contain our logo (attached as PNG and Illustrator file)
- Winning designer must supply a Photoshop file (PSD) that will allow us.
Nice to have
• - Should include photos/images of families, professional groups, tradespeople etc (you can use stock photos from PixQuarry and I will purchase them once you are selected as the winning design)
- Link to a loan calculator somewhere on front page with a button 'Find out how much you could borrow' (or maybe even try adding a loan calculator to the homepage if you think this would look good)
- Page should have a main headline "Finding the right loan for you" or "Brightwell Lending finds the right loan for our customers."
- Must include Accreditation logos somewhere on the homepage (will try and supply these soon)
Should not have
• - Poor quality designs will not be considered
- Do not use clipart

```html
<!DOCTYPE html>
<html lang="en">
<head>
<meta charset="utf-8">
<title>Brightwell Lending</title>
<link href="https://fonts.googleapis.com/css2?family=Questrial&display=swap" rel="stylesheet">
<style>
  :root {
    --cyan: #2eade3;
    --cyan-light: #5ccaf2;
    --blue: #004b70;
    --panel-blue: #005077;
    --text-dark: #2a2a2a;
    --card-border: #bdbdbd;
    --band-grey: #dedede;
    --badge-grey: #c9c9c9;
    --footer-dark: #1c1619;
    --footer-text: #7a7a7a;
    --white: #ffffff;
  }
  * { box-sizing: border-box; margin: 0; padding: 0; }
  html, body {
    width: 1118px; height: 1200px; overflow: hidden;
    background: var(--white);
    font-family: "Questrial", Arial, sans-serif;
    color: var(--text-dark);
  }
  .page { position: relative; width: 1118px; height: 1200px; }

  .top-strip { position: absolute; left: 0; top: 0; width: 100%; height: 7px; background: var(--cyan); }
  .main-nav { position: absolute; left: 475px; top: 0; width: 524px; height: 47px; }
  .main-nav svg { position: absolute; left: 0; top: 0; }
  .main-nav ul { position: absolute; left: 0; top: 0; width: 100%; height: 47px; list-style: none; }
  .main-nav li {
    position: absolute; top: 15px; font-size: 13.5px; color: var(--white);
    transform: translateX(-50%); white-space: nowrap;
  }
  .main-nav li.is-current { color: var(--blue); }

  .brand { position: absolute; left: 152px; top: 80px; width: 250px; height: 120px; }
  .brand-mark { position: absolute; left: 77px; top: 0; width: 60px; height: 60px; border-radius: 50%; background: var(--cyan); }
  .brand-name { position: absolute; left: 0; top: 76px; font-size: 27px; color: var(--cyan); white-space: nowrap; }

  .headline {
    position: absolute; left: 509px; top: 108px; width: 560px;
    font-size: 35.5px; line-height: 45px; font-weight: 400; color: var(--blue);
  }

  .hero { position: absolute; left: 149px; top: 254px; width: 814px; height: 260px; border: 1px solid #bcbcbc; }
  .hero-photo {
    position: absolute; left: 0; top: 0; width: 390px; height: 258px;
    background: linear-gradient(120deg, #8fb0d0 0%, #c9d6e2 35%, #e7e9ec 55%, #9bb8d6 100%);
  }
  .loan-calculator { position: absolute; left: 390px; top: 0; width: 423px; height: 258px; background: var(--panel-blue); }
  .loan-calculator h2 { position: absolute; left: 29px; top: 23px; font-size: 17.5px; font-weight: 400; color: var(--cyan-light); }
  .calc-row { position: absolute; left: 0; width: 423px; height: 28px; }
  .calc-row label { position: absolute; right: 232px; top: 4px; font-size: 16.5px; color: var(--white); white-space: nowrap; }
  .calc-row .field {
    position: absolute; left: 208px; top: 0; width: 174px; height: 28px;
    background: linear-gradient(#e6e6e6, #ffffff 40%); border: 1px solid #cfcfcf;
  }
  .calc-button {
    position: absolute; left: 209px; top: 202px; width: 89px; height: 28px;
    background: var(--cyan); color: var(--white); font-size: 14.5px;
    text-align: center; line-height: 28px;
  }

  .loan-card {
    position: absolute; top: 570px; width: 193px;
    border: 1px solid var(--card-border); border-radius: 6px; overflow: hidden;
    background: linear-gradient(#ffffff, #dadada);
  }
  .loan-card h3 {
    height: 42px; padding-left: 15px; line-height: 43px;
    font-size: 16.5px; font-weight: 400; color: var(--blue);
    background: linear-gradient(var(--cyan-light), var(--cyan));
  }
  .loan-card ul { list-style: none; padding: 20px 12px 0 17px; }
  .loan-card li { font-size: 14px; line-height: 18px; margin-bottom: 10px; }
  .loan-card .more { position: absolute; right: 17px; bottom: 19px; font-size: 12px; color: #444; }
  .card-home { left: 149px; height: 186px; }
  .card-investment { left: 356px; height: 186px; }
  .card-refinancing { left: 565px; height: 225px; }
  .card-business { left: 772px; height: 234px; }

  .accreditation-band { position: absolute; left: 0; top: 873px; width: 100%; height: 159px; background: var(--band-grey); }
  .accreditation-badge {
    position: absolute; top: 45px; width: 152px; height: 72px;
    border-radius: 6px; background: var(--badge-grey);
  }

  .site-footer { position: absolute; left: 0; top: 1032px; width: 100%; height: 168px; background: var(--footer-dark); text-align: center; }
  .footer-mark { position: absolute; left: 536px; top: 38px; width: 46px; height: 46px; border-radius: 50%; background: #4d4a4b; }
  .footer-name { position: absolute; left: 0; width: 100%; top: 92px; font-size: 21px; color: #6e6b6c; }
  .copyright { position: absolute; left: 0; width: 100%; top: 120px; font-size: 10px; color: var(--footer-text); }
</style>
</head>
<body>
<div class="page">
  <div class="top-strip"></div>

  <nav class="main-nav">
    <svg width="524" height="47" viewBox="0 0 524 47" aria-hidden="true">
      <path d="M0 0 H524 L500 40 Q496 47 488 47 H36 Q28 47 24 40 Z" fill="var(--cyan)"/>
    </svg>
    <ul>
      <li class="is-current" style="left:75px">HOME</li>
      <li style="left:160px">SERVICES</li>
      <li style="left:258px">ABOUT US</li>
      <li style="left:342px">FAQ</li>
      <li style="left:432px">CONTACT US</li>
    </ul>
  </nav>

  <div class="brand">
    <div class="brand-mark"></div>
    <div class="brand-name">Brightwell Lending</div>
  </div>

  <h1 class="headline">Brightwell Lending finds the right loan for our customers</h1>

  <section class="hero">
    <div class="hero-photo" role="img" aria-label="Photo of a smiling advisor shaking hands with a couple across a desk"></div>
    <div class="loan-calculator">
      <h2>LOAN CALCULATOR</h2>
      <div class="calc-row" style="top:59px"><label>Loan amount:</label><div class="field"></div></div>
      <div class="calc-row" style="top:94px"><label>Loan term:</label><div class="field"></div></div>
      <div class="calc-row" style="top:130px"><label>Interest rate:</label><div class="field"></div></div>
      <div class="calc-row" style="top:165px"><label>First payment date:</label><div class="field"></div></div>
      <div class="calc-button">Calculate</div>
    </div>
  </section>

  <section class="loan-card card-home">
    <h3>HOME LOAN</h3>
    <ul><li>Home buyers</li><li>First home buyers</li><li>Over 20 lenders</li></ul>
    <span class="more">Click to know more...</span>
  </section>
  <section class="loan-card card-investment">
    <h3>INVESTMENT LOAN</h3>
    <ul><li>Property Investment loans</li><li>Interest only loans</li></ul>
    <span class="more">Click to know more...</span>
  </section>
  <section class="loan-card card-refinancing">
    <h3>REFINANCING</h3>
    <ul><li>Refinancing for the best rate</li><li>Upsizing or downsizing</li><li>Change from a variable to a fixed rate</li></ul>
    <span class="more">Click to know more...</span>
  </section>
  <section class="loan-card card-business">
    <h3>BUSINESS LOAN</h3>
    <ul><li>Business Finance</li><li>Long Term</li><li>Short Term</li><li>Equipment and Leasing</li></ul>
    <span class="more">Click to know more...</span>
  </section>

  <section class="accreditation-band">
    <div class="accreditation-badge" style="left:261px"></div>
    <div class="accreditation-badge" style="left:485px"></div>
    <div class="accreditation-badge" style="left:709px"></div>
  </section>

  <footer class="site-footer">
    <div class="footer-mark"></div>
    <div class="footer-name">Brightwell Lending</div>
    <div class="copyright">Copyright 2012. Brightwell Lending</div>
  </footer>
</div>
</body>
</html>
```